Email Banner (LumenBriefs)

We require an email banner for our email promotions sent to prospect clients. The banner needs to contain the wording LumenBriefs and use the same colour scheme as the logos attached.

This is for B2B professional's so needs to look like a place you would come to read technology articles.

```html
<!DOCTYPE html>
<html lang="en">
<head>
<meta charset="utf-8">
<title>LumenBriefs Email Banners</title>
<link rel="stylesheet" href="https://fonts.googleapis.com/css2?family=Montserrat:wght@500;700;800&family=Catamaran:wght@500;600&display=swap">
<style>
  :root {
    --navy: #041325;
    --ink: #0b1a2a;
    --paper: #ffffff;
    --green: #8dc63f;
    --teal: #24a6a3;
    --blue: #0a95d6;
    --leaf: #5db56a;
  }
  html, body { margin: 0; padding: 0; overflow: hidden; background: var(--paper); }
  .canvas { position: relative; width: 1200px; height: 960px; overflow: hidden; background: var(--paper); }
  .shapes { position: absolute; left: 0; top: 0; width: 1200px; height: 960px; }
  .heading, .brand, .link, .handle { position: absolute; margin: 0; font-family: "Montserrat", sans-serif; white-space: nowrap; }
  .heading { font-size: 17px; font-weight: 800; letter-spacing: -0.2px; }
  .copy {
    position: absolute; margin: 0; font-family: "Catamaran", sans-serif; font-weight: 600;
    font-size: 11.6px; line-height: 17.6px; text-align: justify; text-align-last: left;
  }
  .brand { font-size: 46px; font-weight: 500; letter-spacing: -0.8px; }
  .link { font-size: 18px; font-weight: 700; display: flex; align-items: center; gap: 6px; }
  .handle { font-size: 14.5px; font-weight: 700; }
  .social { position: absolute; display: flex; gap: 9px; }
  .social span { display: block; width: 20px; height: 20px; border-radius: 3px; }

  .on-dark { color: var(--paper); }
  .on-light { color: var(--ink); }
</style>
</head>
<body>
<div class="canvas">
  <svg class="shapes" viewBox="0 0 1000 800" aria-hidden="true">
    <defs>
      <filter id="lift" x="-5%" y="-10%" width="115%" height="130%">
        <feDropShadow dx="4" dy="5" stdDeviation="3" flood-color="#000" flood-opacity="0.28"/>
      </filter>
      <linearGradient id="stripDown" x1="0" y1="0" x2="0" y2="1">
        <stop offset="0" stop-color="var(--leaf)"/>
        <stop offset="0.55" stop-color="var(--teal)"/>
        <stop offset="1" stop-color="var(--blue)"/>
      </linearGradient>
      <linearGradient id="stripUp" x1="0" y1="0" x2="0" y2="1">
        <stop offset="0" stop-color="var(--blue)"/>
        <stop offset="0.45" stop-color="var(--teal)"/>
        <stop offset="1" stop-color="var(--leaf)"/>
      </linearGradient>
      <linearGradient id="bandRight" x1="0" y1="0" x2="1" y2="0">
        <stop offset="0" stop-color="var(--green)"/>
        <stop offset="0.5" stop-color="var(--teal)"/>
        <stop offset="1" stop-color="var(--blue)"/>
      </linearGradient>
      <linearGradient id="bandLeft" x1="0" y1="0" x2="1" y2="0">
        <stop offset="0" stop-color="var(--blue)"/>
        <stop offset="0.5" stop-color="var(--teal)"/>
        <stop offset="1" stop-color="var(--green)"/>
      </linearGradient>
    </defs>

    <!-- banner one -->
    <g class="banner-one">
      <rect x="183" y="76" width="679" height="208" fill="var(--paper)" filter="url(#lift)"/>
      <polygon points="183,76 260,76 185,284 183,284" fill="url(#stripDown)"/>
      <polygon points="260,78 513,78 437,284 185,284" fill="var(--navy)"/>
      <polygon points="452,240 722,240 706,284 437,284" fill="url(#bandRight)"/>
    </g>

    <!-- banner two -->
    <g class="banner-two">
      <rect x="183" y="318" width="679" height="207" fill="var(--paper)" filter="url(#lift)"/>
      <polygon points="183,318 607,318 553,525 183,525" fill="var(--navy)"/>
      <polygon points="330,481 563,481 553,525 314,525" fill="url(#bandLeft)"/>
      <polygon points="859,318 862,318 862,525 805,525" fill="url(#stripUp)"/>
    </g>
  </svg>

  <!-- banner one content -->
  <h2 class="heading on-dark" style="left:318px; top:121px;">BANNER INFORMATION</h2>
  <p class="copy on-dark" style="left:319px; top:152px; width:206px;">Lorem ipsum dolor sit amet, consectetuer adipiscing elit, sed diam nonummy nibh euismod tincidunt ut laoreet dolore magna aliquam erat volutpat. Ut wisi enim ad minim aliquam erat volutpat consectetuer adipiscing elit, sed magna aliquam erat magna aliquam erat ipsum dolor sit amet</p>
  <div class="brand on-light" style="left:598px; top:174px;">LumenBriefs.io</div>
  <div class="link on-light" style="left:646px; top:302px;">
    <svg width="18" height="18" viewBox="0 0 20 20" fill="none" stroke="var(--ink)" stroke-width="1.8"><circle cx="10" cy="10" r="8"/><ellipse cx="10" cy="10" rx="3.6" ry="8"/><path d="M2 10h16"/></svg>Website
  </div>
  <div class="social" style="left:908px; top:289px;">
    <span style="background:var(--teal)"></span><span style="background:var(--teal)"></span><span style="background:var(--blue)"></span>
  </div>
  <div class="handle on-light" style="left:889px; top:312px;">@lumenbriefs</div>

  <!-- banner two content -->
  <h2 class="heading on-light" style="left:744px; top:406px;">BANNER INFORMATION</h2>
  <p class="copy on-light" style="left:744px; top:437px; width:208px;">Lorem ipsum dolor sit amet, consectetuer adipiscing elit, sed diam nonummy nibh euismod tincidunt ut laoreet dolore magna aliquam erat volutpat. Ut wisi enim ad minim aliquam erat volutpat consectetuer adipiscing elit, sed magna aliquam erat magna aliquam erat ipsum dolor sit amet</p>
  <div class="brand on-dark" style="left:262px; top:458px;">LumenBriefs.io</div>
  <div class="link on-dark" style="left:249px; top:589px;">
    <svg width="18" height="18" viewBox="0 0 20 20" fill="none" stroke="var(--paper)" stroke-width="1.8"><circle cx="10" cy="10" r="8"/><ellipse cx="10" cy="10" rx="3.6" ry="8"/><path d="M2 10h16"/></svg>Website
  </div>
  <div class="social" style="left:419px; top:592px;">
    <span style="background:var(--navy)"></span><span style="background:var(--navy)"></span><span style="background:var(--navy)"></span>
  </div>
  <div class="handle on-light" style="left:510px; top:593px; font-size:17px;">@lumenbriefs</div>
</div>
</body>
</html>
```